Business Cards for new orthopaedic surgery practice

My husband and I are starting our own orthopaedic surgery practice. We are looking for a business card that is uniform, but one will have my name/title and the other will have his. You can just create one design with my name on it for now. But when I choose your design as the winning design I will ask that you add another copy with his name/title.

We are looking for classy, simple, elite all in one. We like dark blues/a little gold/yellow. Something that goes with our logo. We want our logo incorporated. Here is all the info you need:
Business name: RV Spine & Vitality Center
Location: 38915 North Bramble Ave
Maple Hollow, FL 33490
Phone: 954-218-4630
Fax: 954-571-2846
Email: info@myrvspine.example

Names: Lucinda Ferrow, M.D.
Board Certified Hand and Upper Extremity Surgeon

Emeka Dlunga, M.D.
Board Certified Hip & Knee Replacement/General Orthopaedic Surgeon

Can decide what you want to put on the back. Maybe a slogan:
Grounded in Care. Centered on You

I am just going to upload our logo. The only thing is if we select you as the winning design, the location, and phone numbers may change. We will need your help to update that once fully solidified.

Industry/Entity Type

Medical

Contact Information for Business Card

Colors
0054AA
0677BA
7BADD7
CADEEF
E8F1F8
0094D4
00A9DD
6FCCEA
C7EBF8
E9F6FB

Requirements
Must have
• class, appeal,
Should not have
• We want to air on the side of masculine if we are looking at masculine vs. feminine feel. But we still want it classy, sophisticated, and something we will love

```html
<!DOCTYPE html>
<html lang="en">
<head>
<meta charset="utf-8">
<title>RV Spine &amp; Vitality Center — Business Card</title>
<link href="https://fonts.googleapis.com/css2?family=Barlow:wght@400;500;700&display=swap" rel="stylesheet">
<style>
  :root {
    --navy: #2c3a5f;
    --gold: #c9a96a;
    --white: #fbfbfb;
    --ink: #2a2f3a;
    --backdrop: #e7e5e0;
  }
  * { box-sizing: border-box; margin: 0; padding: 0; }
  html, body {
    width: 1200px; height: 840px; overflow: hidden;
    background: var(--backdrop);
    font-family: "Barlow", Arial, sans-serif;
  }
  .canvas { position: relative; width: 1200px; height: 840px; }
  .card {
    position: absolute; width: 560px; height: 320px; overflow: hidden;
    box-shadow: 0 10px 28px rgba(0,0,0,.18);
  }
  /* Front */
  .card-front { left: 580px; top: 80px; background: var(--white); }
  .front-bands { position: absolute; left: 0; top: 0; }
  .contact { position: absolute; left: 44px; top: 46px; color: var(--ink); }
  .contact-name {
    color: var(--navy); font-weight: 700; font-size: 26px;
    letter-spacing: .5px; text-transform: uppercase; line-height: 1;
  }
  .contact-title { font-size: 17px; line-height: 1.15; margin-top: 6px; }
  .contact-list { list-style: none; margin-top: 10px; font-size: 17px; line-height: 1.4; }
  .contact-list li { display: flex; align-items: center; gap: 10px; }
  .contact-list svg { width: 14px; height: 14px; flex: none; }
  .contact-address { font-size: 17px; line-height: 1.2; margin-top: 8px; }
  .front-brand {
    position: absolute; right: 34px; top: 70px; width: 170px;
    display: flex; flex-direction: column; align-items: center; gap: 12px;
    text-align: center;
  }
  .brand-dot { width: 22px; height: 22px; border-radius: 50%; background: var(--navy); }
  .front-brand .brand-name {
    color: var(--navy); font-weight: 700; font-size: 24px; line-height: 1.1;
    text-transform: uppercase; letter-spacing: 1px;
  }
  /* Back */
  .card-back {
    left: 60px; top: 440px; background: var(--navy);
    display: flex; flex-direction: column; align-items: center; justify-content: center;
  }
  .back-brand { display: flex; flex-direction: column; align-items: center; gap: 14px; }
  .back-brand .brand-dot { background: var(--white); width: 20px; height: 20px; }
  .back-brand .brand-name {
    color: var(--white); font-weight: 500; font-size: 24px;
    letter-spacing: 3px; text-transform: uppercase; text-align: center; line-height: 1.25;
  }
  .slogan { margin-top: 38px; color: var(--gold); font-size: 19px; letter-spacing: .5px; }
</style>
</head>
<body>
<main class="canvas">

  <section class="card card-front" aria-label="Business card front">
    <svg class="front-bands" width="560" height="320" viewBox="0 0 560 320" aria-hidden="true">
      <polygon points="0,272 300,272 320,320 0,320" fill="var(--gold)"/>
      <polygon points="310,272 560,272 560,320 330,320" fill="var(--navy)"/>
    </svg>

    <div class="contact">
      <h1 class="contact-name">Lucinda Ferrow, M.D.</h1>
      <p class="contact-title">Board Certified Hand and<br>Upper Extremity Surgeon</p>
      <ul class="contact-list">
        <li>
          <svg viewBox="0 0 16 16" aria-label="Phone"><path fill="var(--gold)" d="M3.5 1l2.5 3-1.5 1.8c.8 2 2.2 3.5 4.2 4.3L10.5 8.6l3 2.5-1.3 2.7C7.5 14 2 8.5 1.2 3.2z"/></svg>
          954-218-4630
        </li>
        <li>
          <svg viewBox="0 0 16 16" aria-label="Fax"><rect x="4" y="1" width="8" height="4" fill="var(--gold)"/><rect x="1" y="6" width="14" height="6" rx="1" fill="var(--gold)"/><rect x="4" y="10" width="8" height="5" fill="var(--gold)" stroke="var(--white)" stroke-width="1"/></svg>
          954-571-2846
        </li>
        <li>
          <svg viewBox="0 0 16 16" aria-label="Web"><g fill="none" stroke="var(--gold)" stroke-width="1.3"><circle cx="8" cy="8" r="6.5"/><ellipse cx="8" cy="8" rx="3" ry="6.5"/><path d="M1.5 8h13"/></g></svg>
          info@myrvspine.example
        </li>
      </ul>
      <p class="contact-address">38915 North Bramble Ave<br>Maple Hollow, FL 33490</p>
    </div>

    <div class="front-brand">
      <span class="brand-dot"></span>
      <span class="brand-name">RV Spine &amp; Vitality Center</span>
    </div>
  </section>

  <section class="card card-back" aria-label="Business card back">
    <div class="back-brand">
      <span class="brand-dot"></span>
      <span class="brand-name">RV Spine &amp;<br>Vitality Center</span>
    </div>
    <p class="slogan">Grounded in Care. Centered on You</p>
  </section>

</main>
</body>
</html>
```